Rudy Fenwick - Free Personalised Health Consultation - "One size does not fit all"

This flyer will be left on tables/seats at speaking events and seminars and used to attain leads.

Top half will have "SMS me for a FREE Personalised Health Consultation" and my picture (see www.rudyfenwick.example and pick most engaging photo) and underneath my contact details. It must have lines with "Notes:" halfway down so people can take notes at the seminar and lines on the back with my contact details again and "Notes: with lines.

I am having a business card also being designed by Artshelf for same and would like the flyer and business card to carry a similar feel/look for consistency.

Below is the brief for the business card being designed:
Business Card for www.rudyfenwick.example site. It is a trust site and I use it for 1:1 relatable connections. It is the one I use for building intimate 1:1 trust building and Exec Coaching Services and programs for high wealth individuals and corporates. I also have a commercial programmatic site of my personal health products and services and programs for main stream one to many. www.quietbirchliving.example that can also provoke thought for the www.rudyfenwick.example business card. (mind you will get a separate business card for that site, but want to provide context). It has a logo which you may want to draw from in designing the rudyfenwick business card which is personal and is about building my brand. There is also a rudyfenwick personal FB page and rudyfenwick business FB page. I am a Certified Talent Compass 3.1 Coach with Harlow and you can get a corporate brief of me on there to give you more context https://www.harlowtalenthub.example/coach/en-us/directory?search=rudy

Target Market(s)

Exec, IT, Health conscious. Corporates wanting to run Health and Wellness programs. Those wanting to go from good to great. Millennials to Middleaged.

Industry/Entity Type

Health And Wellness

Font styles to use
Sans Serif
Other font styles liked:
• Arial and Calibri ok too

Colors

Designer to choose colors to be used in the design.

Requirements
Must have
• Picture of me - use best from www.rudyfenwick.example or can send one you choose.
• Contact details like my buisness card being designed by you guys in separate project.
• Name: Rudy Fenwick
• email: rudy@rudyfenwick.,example
• Phone: Australia +61 400 000 000 Singapore: +65 9000 0000
Nice to have
• Open to ideas

```html
<!DOCTYPE html>
<html lang="en">
<head>
<meta charset="utf-8">
<title>Rudy Fenwick – Free Personalised Health Consultation</title>
<link rel="stylesheet" href="https://fonts.googleapis.com/css2?family=Montserrat:wght@400;500;700&family=Roboto:wght@400;500;700&family=Nothing+You+Could+Do&display=swap">
<style>
  :root {
    --ink: #1e1e1e;
    --header-bg: #1d1d1d;
    --profile-bg: #ebebeb;
    --contact-bg: #2e2b2c;
    --paper: #f7f7f7;
    --ribbon: #bdbdbd;
    --rule: #c9c9c9;
    --muted: #6f6f6f;
    --soft-white: #d9d9d9;
    --white: #ffffff;
  }
  * { box-sizing: border-box; margin: 0; padding: 0; }
  html, body { width: 848px; height: 1200px; overflow: hidden; background: var(--paper); }
  .flyer { position: relative; width: 848px; height: 1200px; background: var(--paper); font-family: "Montserrat", Arial, sans-serif; }

  .headline {
    position: absolute; left: 0; top: 0; width: 848px; height: 118px;
    background: var(--header-bg); color: var(--white);
    display: flex; flex-direction: column; justify-content: center; align-items: center;
    font-weight: 700; font-size: 29.5px; line-height: 37px; text-align: center; letter-spacing: 0.2px;
    padding-top: 2px;
  }

  .profile { position: absolute; left: 0; top: 118px; width: 413px; height: 394px; background: var(--profile-bg); }
  .portrait {
    position: absolute; left: 126px; top: 69px; width: 190px; height: 190px; border-radius: 50%;
    border: 3px solid #111;
    background: radial-gradient(circle at 50% 40%, #cfcfcf 0%, #9a9a9a 45%, #2a2a2a 100%);
  }
  .profile-name {
    position: absolute; left: 0; width: 442px; top: 268px; text-align: center;
    font-weight: 700; font-size: 31.5px; color: var(--ink); letter-spacing: 0.3px;
  }
  .profile-role {
    position: absolute; left: 0; width: 442px; top: 302px; text-align: center;
    font-weight: 400; font-size: 20.5px; color: var(--muted);
  }

  .contact { position: absolute; left: 413px; top: 118px; width: 435px; height: 394px; background: var(--contact-bg); color: var(--white); }
  .signature {
    position: absolute; left: 22px; top: 12px;
    font-family: "Nothing You Could Do", cursive; font-size: 42px; color: var(--white); letter-spacing: 1px;
  }
  .expertise {
    position: absolute; left: 22px; top: 86px; width: 345px;
    font-family: "Roboto", Arial, sans-serif; font-size: 12.6px; line-height: 15.5px; color: var(--soft-white);
  }
  .expertise strong { font-weight: 700; color: var(--white); }
  .divider { position: absolute; left: 124px; top: 175px; width: 111px; height: 2px; background: #b5b5b5; }

  .icon-ribbon { position: absolute; left: -10px; top: 204px; }
  .details { position: absolute; left: 47px; top: 212px; font-family: "Roboto", Arial, sans-serif; font-size: 18.5px; color: var(--white); list-style: none; }
  .details li { position: absolute; left: 0; white-space: nowrap; }

  .notes-tab { position: absolute; left: 226px; top: 500px; }
  .notes-label {
    position: absolute; left: 233px; top: 509px; width: 384px; text-align: center;
    font-weight: 700; font-size: 22px; color: var(--white); letter-spacing: 0.5px;
  }
  .note-lines { position: absolute; left: 52px; top: 589px; width: 743px; }
  .note-lines span { display: block; height: 1.5px; background: var(--rule); margin-bottom: 48.3px; }
</style>
</head>
<body>
<main class="flyer">
  <header class="headline">
    <span>SMS ME FOR A</span>
    <span>FREE PERSONALISED HEALTH CONSULTATION</span>
  </header>

  <section class="profile">
    <div class="portrait" role="img" aria-label="Portrait photo of Rudy Fenwick"></div>
    <h1 class="profile-name">RUDY FENWICK</h1>
    <p class="profile-role">Coachng Expert</p>
  </section>

  <section class="contact">
    <p class="signature">Rudy Fenwick</p>
    <p class="expertise"><strong>Coaching Expertise:</strong> Career, Enterprise Business, Executive Coaching, Healthcare, Keynotes, Leadership, Managers, Personal Development, Sales, Small Business/Entrepreneurs, Students/Youth, Teams, Technology, Wellbeing</p>
    <div class="divider"></div>

    <svg class="icon-ribbon" width="26" height="164" viewBox="0 0 26 164" aria-hidden="true">
      <polygon points="0,8 10,0 26,0 26,164 10,164 0,156" fill="var(--ribbon)"/>
      <!-- phone -->
      <g fill="none" stroke="#fff" stroke-width="2" stroke-linecap="round">
        <path d="M9 20 q-2 6 2 12"/>
        <path d="M15 21 q2 5 0 10"/>
        <path d="M18.5 19 q3 7 0 14"/>
      </g>
      <rect x="6" y="18" width="6" height="16" rx="2" fill="#fff"/>
      <!-- at -->
      <text x="14.5" y="82" text-anchor="middle" font-family="Roboto, Arial, sans-serif" font-weight="700" font-size="19" fill="#fff">@</text>
      <!-- globe -->
      <g fill="none" stroke="#fff" stroke-width="1.8">
        <circle cx="14.5" cy="106" r="9"/>
        <ellipse cx="14.5" cy="106" rx="4" ry="9"/>
        <line x1="5.5" y1="106" x2="23.5" y2="106"/>
        <line x1="7" y1="101" x2="22" y2="101"/>
        <line x1="7" y1="111" x2="22" y2="111"/>
      </g>
      <!-- pin -->
      <path d="M14.5 145 C9 138 6 134 6 130 a8.5 8.5 0 0 1 17 0 c0 4 -3 8 -8.5 15z" fill="#fff"/>
      <circle cx="14.5" cy="130" r="3.2" fill="var(--ribbon)"/>
    </svg>

    <ul class="details">
      <li style="top:0">Australia: +61 400 000 000</li>
      <li style="top:24px">Singapore: +65 9000 0000</li>
      <li style="top:55px">rudy@rudyfenwick.,example</li>
      <li style="top:83px">www.rudyfenwick.,example</li>
      <li style="top:112px">48 Alder Lane, Eastvale</li>
    </ul>
  </section>

  <svg class="notes-tab" width="396" height="48" viewBox="0 0 396 48" aria-hidden="true">
    <polygon points="0,12 7,2 10,12" fill="#111"/>
    <polygon points="396,12 389,2 386,12" fill="#111"/>
    <polygon points="7,2 389,2 381,45 17,45" fill="#c0c0c0"/>
  </svg>
  <h2 class="notes-label">NOTES</h2>

  <div class="note-lines" aria-hidden="true">
    <span></span><span></span><span></span><span></span><span></span><span></span>
    <span></span><span></span><span></span><span></span><span></span><span></span>
  </div>
</main>
</body>
</html>
```